REDESIGN SIGN UP PAGE - EASY TO READ AND UNDERSTAND QUICKLY

I need to redesign my sign up page DESKTOP AND MOBILE VERSION to include 2 products that are each available as a monthly subscription, 6 mth or 12 mth subscription.

Currently I only promote one product on my website but now will be two. https://www.brightlanepromoworks.biz/signup

Now I will have two products:

1. UNLIMITED VACATION CERTIFICATES, DINING VOUCHERS & SAVINGS INCENTIVES
Unlimited Monthly Plan $99 / Month + $199 One-Time Set-Up Fee
Unlimited Bi Annual Plan $490 / 6 Months + $199 One-Time Set-Up Fee
Unlimited Annual Plan $898 / 12 Months + $199 One-Time Set-Up Fee

2. UNLIMITED SMART DEVICE INCENTIVES & OTHER HARD PREMIUMS
Unlimited Monthly Plan $299 / Month + $199 One-Time Set-Up Fee
Unlimited Bi Annual Plan $1,590 / 6 Months + $199 One-Time Set-Up Fee
Unlimited Annual Plan $2,898 / 12 Months + $199 One-Time Set-Up Fee

When promoting the different plans you can see the different categories of incentives I offer here: https://www.brightlanepromoworks.biz/incentives

The SMART DEVICE CERTIFICATES & INCENTIVES category is for product #2 and all the rest of the Categories is for Product #1 Feel free to use images as a visual so customers can see that this product includes Vacations & Restaurants and this product includes only smart devices....

USE ALL CURRENT BULLET POINTS FOR BOTH PLANS THAT IS CURRENTLY ON WEBSITE. USE ALL CURRENT CONTENT ON WEBSITE ORIGINAL SIGN UP PAGE. DO NOT LEAVE ANY CONTENT OUT.

Target Market(s)

BUSINESS OWNERS

Industry/Entity Type

Marketing

Number of Pages Required

2 page

Requirements
Must have
• When promoting the 2 different products on the new sign up page you can see the different categories of incentives I offer here: https://www.brightlanepromoworks.biz/incentives fee; free to use images to showcase what each product offers.

The SMART DEVICE CERTIFICATES & INCENTIVES category is for product #2 and all the rest of the Categories is for Product #1

I want the user to easily understand we have two products that are available in 3 ways, monthly subscription, bi annual and annual and can see the price immediately for all 3 options for both products without toggling, etc.

Must be super clean easy to ready design. Not too busy at all please
Nice to have
• USE ALL CURRENT BULLET POINTS FOR BOTH PLANS THAT IS CURRENTLY ON WEBSITE. USE ALL CURRENT CONTENT ON WEBSITE ORIGINAL SIGN UP PAGE. DO NOT LEAVE ANY CONTENT OUT.

Should not have

```html
<!DOCTYPE html>
<html lang="en">
<head>
<meta charset="utf-8">
<title>Sign Up – Brightlane Promo Works</title>
<link href="https://fonts.googleapis.com/css2?family=Montserrat:wght@800;900&family=Poppins:wght@400;500;600;700&display=swap" rel="stylesheet">
<style>
:root{
  --blue:#1a73c9;
  --blue-dark:#0f4f91;
  --green:#3dae4a;
  --green-bright:#4cbb3a;
  --ink:#1c1c1c;
  --text:#444;
  --orange:#f7a21b;
  --tint:#f4f7fb;
  --nav-dark:#4b4f55;
  --footer:#10233a;
  --footer-text:#c9d2dc;
  --white:#fff;
}
*{box-sizing:border-box;margin:0;padding:0}
html,body{width:1200px;height:2993px;overflow:hidden;background:var(--white)}
body{font-family:"Poppins",sans-serif;color:var(--text);position:relative}

/* header */
.site-header{position:absolute;left:0;top:0;width:1200px;height:79px}
.brand{position:absolute;left:16px;top:29px;display:flex;align-items:center;gap:7px;font:600 13px/1 "Poppins",sans-serif;color:var(--blue);letter-spacing:.3px;white-space:nowrap}
.brand-dot{width:22px;height:22px;border-radius:50%;background:var(--blue)}
.main-nav{position:absolute;left:253px;top:0;width:621px;height:79px;background:var(--blue);clip-path:polygon(24px 0,100% 0,100% 100%,0 100%);display:flex;align-items:center;gap:23px;padding-left:62px}
.main-nav a{color:var(--white);font:500 12px "Poppins",sans-serif;text-decoration:none}
.account{position:absolute;top:0;height:79px;width:61px;color:var(--white);font:500 10px "Poppins",sans-serif;display:flex;flex-direction:column;align-items:center;justify-content:center;gap:5px;text-decoration:none}
.account.login{left:874px;background:var(--nav-dark)}
.account.signup{left:935px;background:var(--blue)}
.call-box{position:absolute;left:996px;top:0;width:204px;height:79px;background:var(--green-bright);color:var(--white);font:700 12px/1.5 "Poppins",sans-serif;display:flex;align-items:center;gap:10px;padding-left:10px}

/* hero */
.hero-icon{position:absolute;left:541px;top:141px;width:118px;height:118px;border-radius:50%;background:var(--blue);border:6px solid #dfe6ee;display:flex;align-items:center;justify-content:center}
.hero-title{position:absolute;left:0;top:273px;width:1200px;text-align:center;font:900 37px/46px "Montserrat",sans-serif;color:var(--ink);letter-spacing:-.5px;text-transform:uppercase}
.hero-title span{color:var(--blue)}

/* both products shown side by side */
.products-bar{position:absolute;left:0;top:486px;width:1200px;height:54px;display:flex}
.product-tag{flex:1;display:flex;align-items:center;justify-content:center;gap:10px;font:600 18px "Poppins",sans-serif;color:var(--white)}
.product-tag.one{background:var(--blue)}
.product-tag.two{background:var(--blue-dark)}
.product-tag i{font-style:normal;width:24px;height:24px;border-radius:50%;background:var(--white);font:700 13px/24px "Poppins",sans-serif;text-align:center}
.product-tag.one i{color:var(--blue)}
.product-tag.two i{color:var(--blue-dark)}

.product-title{position:absolute;left:0;top:598px;width:1200px;text-align:center;font:900 27px/37px "Montserrat",sans-serif;color:var(--green);text-transform:uppercase;letter-spacing:-.3px}

/* categories */
.category{position:absolute;top:716px;width:222px}
.category-photo{margin-left:9px;width:204px;height:181px}
.category-label{height:63px;background:var(--blue);color:var(--white);font:500 15px/19px "Poppins",sans-serif;display:flex;align-items:center;justify-content:center;text-align:center;padding:0 8px;clip-path:polygon(0 0,100% 0,100% 88%,50% 100%,0 88%)}
.category.device .category-label{background:var(--blue-dark)}

.intro{position:absolute;left:0;top:1016px;width:1200px;text-align:center;font:400 26px/33px "Poppins",sans-serif;color:var(--ink)}

/* plans */
.plan{position:absolute;top:1140px;width:360px;height:1290px;background:var(--white);box-shadow:0 2px 12px rgba(0,0,0,.12)}
.plan-head{height:82px;padding:17px 18px 0;background:var(--tint);clip-path:polygon(0 0,93% 0,100% 50%,93% 100%,0 100%)}
.plan.featured .plan-head{background:var(--blue);clip-path:none}
.plan-name{font:700 21px "Poppins",sans-serif;color:var(--blue);letter-spacing:.3px;white-space:nowrap}
.plan-name em{font-style:normal;color:var(--orange)}
.plan-sub{font:500 12px "Poppins",sans-serif;color:var(--blue);margin-top:4px}
.plan.featured .plan-name,.plan.featured .plan-sub{color:var(--white)}
.plan-body{padding:0 18px}

.offer{padding:14px 0 16px;border-bottom:1px solid #e4e4e4}
.offer-label{display:flex;align-items:center;gap:7px;font:600 12px "Poppins",sans-serif;color:var(--blue);text-transform:uppercase;letter-spacing:.3px}
.offer-label i{font-style:normal;width:18px;height:18px;border-radius:50%;background:var(--blue);color:var(--white);font:700 10px/18px "Poppins",sans-serif;text-align:center}
.offer.two .offer-label{color:var(--blue-dark)}
.offer.two .offer-label i{background:var(--blue-dark)}
.price{margin-top:4px;display:flex;align-items:baseline;font:400 13px "Poppins",sans-serif;color:#333;white-space:nowrap}
.price .cur{font-size:22px;color:var(--blue);margin-right:2px}
.price .amt{font:600 36px/44px "Poppins",sans-serif;color:var(--blue);margin-right:5px}
.fee{font:400 12px "Poppins",sans-serif;color:#333}
.fee b{color:var(--blue);font-weight:600;font-size:13px}
.offer-row{display:flex;align-items:flex-end;justify-content:space-between}

.btn-select{display:flex;align-items:center;justify-content:center;gap:12px;width:176px;height:62px;background:var(--blue);color:var(--white);font:600 25px "Poppins",sans-serif;border-radius:2px;text-decoration:none}
.btn-select.small{width:122px;height:44px;font-size:18px;gap:8px;flex:none}
.offer.two .btn-select.small{background:var(--blue-dark)}

.features-title{margin-top:24px;padding-bottom:12px;border-bottom:1px solid #e4e4e4;font:500 18px "Poppins",sans-serif;color:var(--blue)}
.features{list-style:none;margin-top:16px}
.features li{position:relative;padding-left:23px;font:400 14px/18px "Poppins",sans-serif;color:#333;margin-bottom:12px}
.features li::before{content:"";position:absolute;left:3px;top:1px;width:6px;height:11px;border:solid var(--blue);border-width:0 3px 3px 0;transform:rotate(45deg)}
.bottom-select{position:absolute;left:18px;bottom:24px}

/* footer */
.site-footer{position:absolute;left:0;top:2469px;width:1200px;height:524px;background:var(--footer);color:var(--footer-text);font:400 13.5px/19px "Poppins",sans-serif}
.footer-brand{position:absolute;left:14px;top:78px;display:flex;align-items:center;gap:8px;font:600 17px "Poppins",sans-serif;color:var(--blue);white-space:nowrap}
.footer-brand .dot{width:26px;height:26px;border-radius:50%;background:var(--blue);flex:none}
.socials{position:absolute;left:49px;top:183px;display:flex;gap:10px}
.socials span{width:43px;height:43px;border-radius:50%;background:#8b96a3}
.free-samples{position:absolute;left:17px;top:251px;width:265px;height:60px;background:var(--green-bright);color:var(--white);text-align:center;font:800 14px/18px "Montserrat",sans-serif;padding-top:12px;clip-path:polygon(0 0,100% 0,100% 85%,50% 100%,0 85%)}
.free-samples small{display:block;font:500 13px "Poppins",sans-serif}
.fcol{position:absolute;top:70px}
.fcol h4{font:900 17px "Montserrat",sans-serif;color:var(--white);text-transform:uppercase;letter-spacing:.3px;margin-bottom:20px}
.fdivider{position:absolute;top:60px;width:1px;height:240px;background:#28394d}
.links a{display:block;color:var(--footer-text);text-decoration:none;margin-bottom:9px}
.contact-row{position:relative;padding-left:27px;margin-bottom:9px}
.contact-row svg{position:absolute;left:0;top:2px}
.contact-row strong{color:var(--white);font-weight:600}
.green-note{color:var(--green-bright)}
.copyright{position:absolute;left:14px;top:484px;font-size:14px}
.copyright strong{color:var(--white)}
.copyright .tc{color:var(--blue)}
.legal{position:absolute;right:14px;top:484px;font-size:14px}
.chat{position:absolute;left:1109px;top:452px;width:54px;height:54px;border-radius:50%;background:#e5231f;display:flex;align-items:center;justify-content:center}
</style>
</head>
<body>

<header class="site-header">
  <div class="brand"><span class="brand-dot"></span>BRIGHTLANE PROMO WORKS</div>
  <nav class="main-nav">
    <a href="#">Home</a><a href="https://www.brightlanepromoworks.biz/incentives">The Incentives</a><a href="#">Samples</a><a href="#">Industries</a><a href="#">Testimonials</a><a href="#">Faq</a><a href="#">Integrations</a>
  </nav>
  <div class="account login">
    <svg width="18" height="18" viewBox="0 0 18 18"><circle cx="9" cy="5" r="4" fill="#fff"/><path d="M1 17c0-5 16-5 16 0z" fill="#fff"/></svg>LOGIN</div>
  <a class="account signup" href="https://www.brightlanepromoworks.biz/signup">
    <svg width="18" height="18" viewBox="0 0 18 18"><circle cx="9" cy="9" r="7.5" fill="none" stroke="#fff" stroke-width="1.5"/><path d="M9 13V5M6 8l3-3 3 3" stroke="#fff" stroke-width="1.5" fill="none"/></svg>SIGN UP</a>
  <div class="call-box">
    <svg width="22" height="40" viewBox="0 0 22 40"><rect x="2" y="1" width="18" height="38" rx="3" fill="none" stroke="#fff" stroke-width="2.5"/><circle cx="11" cy="33" r="2" fill="#fff"/></svg>
    <div>CALL US: 1-555-214-3780<br>TEXT US: 1-555-302-7719</div>
  </div>
</header>

<div class="hero-icon">
  <svg width="64" height="60" viewBox="0 0 64 60" fill="none" stroke="#fff" stroke-width="3.5" stroke-linejoin="round">
    <rect x="6" y="28" width="12" height="26"/>
    <path d="M18 30l10-12 2-12c6 0 8 6 6 16h14c4 0 5 5 2 7 3 2 2 6-1 7 2 2 1 6-2 7 1 3-1 6-4 6H18"/>
    <path d="M40 6l2-5M48 10l4-3M30 4l-2-4" stroke-linecap="round"/>
  </svg>
</div>

<h1 class="hero-title">Congratulations on making the<br>decision to <span>make more money for<br>your business</span></h1>

<div class="products-bar">
  <div class="product-tag one"><i>1</i>VACATION, DINING &amp; SAVINGS INCENTIVES</div>
  <div class="product-tag two"><i>2</i>SMART DEVICE INCENTIVES &amp; OTHER HARD PREMIUMS</div>
</div>

<h2 class="product-title">Unlimited vacation, dining &amp; savings incentives<br>+ smart device incentives &amp; hard premiums</h2>

<div class="category" style="left:27px">
  <div class="category-photo" role="img" aria-label="Aerial photo of a tropical beach and coastline" style="background:linear-gradient(135deg,#c98a5c,#8a6a4a 45%,#2f6e74 75%,#1d4f5c)"></div>
  <div class="category-label">Vacation Certificates &amp; Incentives</div>
</div>
<div class="category" style="left:258px">
  <div class="category-photo" role="img" aria-label="Diners gathered at restaurant tables" style="background:linear-gradient(135deg,#d9d2c6,#7e6e5c 50%,#3e352c)"></div>
  <div class="category-label">Dining &amp; Restaurant Certificates, Vouchers &amp; Incentives</div>
</div>
<div class="category" style="left:489px">
  <div class="category-photo" role="img" aria-label="Resort building reflected in a pool at dusk" style="background:linear-gradient(180deg,#2f4f86,#7f93b8 45%,#c9a27a 60%,#1f3a6a)"></div>
  <div class="category-label">Resort Certificates &amp; Incentives</div>
</div>
<div class="category" style="left:720px">
  <div class="category-photo" role="img" aria-label="Cruise ship at sea under an orange sunset" style="background:linear-gradient(180deg,#f2a860,#e98a4a 45%,#b8694a 65%,#5a4a4e)"></div>
  <div class="category-label">Cruise Certificates &amp; Incentives</div>
</div>
<div class="category device" style="left:951px">
  <div class="category-photo" role="img" aria-label="Smart phones, tablets and headphones on a desk" style="background:linear-gradient(135deg,#cfd8e3,#7d8ea3 50%,#2c3a4d)"></div>
  <div class="category-label">Smart Device Certificates &amp; Incentives</div>
</div>

<p class="intro">This program is an online subscription based incentive<br>marketing system with the following features</p>

<section class="plan" style="left:31px">
  <div class="plan-head"><div class="plan-name">UNLIMITED <em>MONTHLY</em> PLAN</div><div class="plan-sub">One Account Can Be Used For Unlimited Brands</div></div>
  <div class="plan-body">
    <div class="offer one">
      <div class="offer-label"><i>1</i>Vacation, Dining &amp; Savings</div>
      <div class="offer-row"><div><div class="price"><span class="cur">$</span><span class="amt">99</span>/ month</div><div class="fee">+ <b>$199</b> One-time Set-up fee</div></div>
      <a class="btn-select small" href="#">SELECT <svg width="16" height="14" viewBox="0 0 20 18"><path d="M1 9h16M10 2l7 7-7 7" stroke="#fff" stroke-width="3" fill="none"/></svg></a></div>
    </div>
    <div class="offer two">
      <div class="offer-label"><i>2</i>Smart Devices &amp; Hard Premiums</div>
      <div class="offer-row"><div><div class="price"><span class="cur">$</span><span class="amt">299</span>/ month</div><div class="fee">+ <b>$199</b> One-time Set-up fee</div></div>
      <a class="btn-select small" href="#">SELECT <svg width="16" height="14" viewBox="0 0 20 18"><path d="M1 9h16M10 2l7 7-7 7" stroke="#fff" stroke-width="3" fill="none"/></svg></a></div>
    </div>
    <div class="features-title">UNLIMITED CERTIFICATE TYPES</div>
    <ul class="features">
      <li>Unlimited E-Certificates</li><li>Unlimited SMS Certificates</li><li>Unlimited Web Banner Certificates</li><li>Unlimited White Label Certiifcate Landing Pages</li><li>Unlimited Website Sticky Bar Certificates</li><li>Unlimited Website Pop Up Certificate</li><li>Unlimited API E-Certificates</li><li>Unlimited Flowlink Integration Access</li><li>FREE Warm Lead Letter Templates</li><li>FREE Customer Appreciation Letter Templates</li><li>FREE Professional-Grade Incentive Videos</li><li>FREE Proven Social Feed Ad Templates</li><li>FREE High-Converting Banner Ad Templates</li><li>FREE Time-Tested Print Ad Templates</li><li>FREE White Label Redemption Website</li><li>FREE Industry Specific Ad Packs</li><li>FREE Affiliate Program-Earn 50% Commissions</li><li>FREE Eye-Catching Posters, Flyers &amp; Brochures Each Certificate</li><li>FREE Step by Step Redemption Guides</li>
    </ul>
  </div>
  <a class="btn-select bottom-select" href="#">SELECT <svg width="20" height="18" viewBox="0 0 20 18"><path d="M1 9h16M10 2l7 7-7 7" stroke="#fff" stroke-width="3" fill="none"/></svg></a>
</section>

<section class="plan featured" style="left:420px">
  <div class="plan-head"><div class="plan-name">UNLIMITED <em>BI ANNUAL</em> PLAN</div><div class="plan-sub">One Account Can Be Used For Unlimited Brands</div></div>
  <div class="plan-body">
    <div class="offer one">
      <div class="offer-label"><i>1</i>Vacation, Dining &amp; Savings</div>
      <div class="offer-row"><div><div class="price"><span class="cur">$</span><span class="amt">490</span>/ 6 months</div><div class="fee">+ <b>$199</b> One-time Set-up fee</div></div>
      <a class="btn-select small" href="#">SELECT <svg width="16" height="14" viewBox="0 0 20 18"><path d="M1 9h16M10 2l7 7-7 7" stroke="#fff" stroke-width="3" fill="none"/></svg></a></div>
    </div>
    <div class="offer two">
      <div class="offer-label"><i>2</i>Smart Devices &amp; Hard Premiums</div>
      <div class="offer-row"><div><div class="price"><span class="cur">$</span><span class="amt">1,590</span>/ 6 months</div><div class="fee">+ <b>$199</b> One-time Set-up fee</div></div>
      <a class="btn-select small" href="#">SELECT <svg width="16" height="14" viewBox="0 0 20 18"><path d="M1 9h16M10 2l7 7-7 7" stroke="#fff" stroke-width="3" fill="none"/></svg></a></div>
    </div>
    <div class="features-title">UNLIMITED CERTIFICATE TYPES</div>
    <ul class="features">
      <li>Unlimited E-Certificates</li><li>Unlimited SMS Certificates</li><li>Unlimited Web Banner Certificates</li><li>Unlimited White Label Certiifcate Landing Pages</li><li>Unlimited Website Sticky Bar Certificates</li><li>Unlimited Website Pop Up Certificate</li><li>Unlimited API E-Certificates</li><li>Unlimited Flowlink Integration Access</li><li>FREE Warm Lead Letter Templates</li><li>FREE Customer Appreciation Letter Templates</li><li>FREE Professional-Grade Incentive Videos</li><li>FREE Proven Social Feed Ad Templates</li><li>FREE High-Converting Banner Ad Templates</li><li>FREE Time-Tested Print Ad Templates</li><li>FREE White Label Redemption Website</li><li>FREE Industry Specific Ad Packs</li><li>FREE Affiliate Program-Earn 50% Commissions</li><li>FREE Eye-Catching Posters, Flyers &amp; Brochures Each Certificate</li><li>FREE Step by Step Redemption Guides</li>
    </ul>
  </div>
  <a class="btn-select bottom-select" href="#">SELECT <svg width="20" height="18" viewBox="0 0 20 18"><path d="M1 9h16M10 2l7 7-7 7" stroke="#fff" stroke-width="3" fill="none"/></svg></a>
</section>

<section class="plan" style="left:809px">
  <div class="plan-head"><div class="plan-name">UNLIMITED <em>ANNUAL</em> PLAN</div><div class="plan-sub">One Account Can Be Used For Unlimited Brands</div></div>
  <div class="plan-body">
    <div class="offer one">
      <div class="offer-label"><i>1</i>Vacation, Dining &amp; Savings</div>
      <div class="offer-row"><div><div class="price"><span class="cur">$</span><span class="amt">898</span>/ 12 months</div><div class="fee">+ <b>$199</b> One-time Set-up fee</div></div>
      <a class="btn-select small" href="#">SELECT <svg width="16" height="14" viewBox="0 0 20 18"><path d="M1 9h16M10 2l7 7-7 7" stroke="#fff" stroke-width="3" fill="none"/></svg></a></div>
    </div>
    <div class="offer two">
      <div class="offer-label"><i>2</i>Smart Devices &amp; Hard Premiums</div>
      <div class="offer-row"><div><div class="price"><span class="cur">$</span><span class="amt">2,898</span>/ 12 months</div><div class="fee">+ <b>$199</b> One-time Set-up fee</div></div>
      <a class="btn-select small" href="#">SELECT <svg width="16" height="14" viewBox="0 0 20 18"><path d="M1 9h16M10 2l7 7-7 7" stroke="#fff" stroke-width="3" fill="none"/></svg></a></div>
    </div>
    <div class="features-title">UNLIMITED CERTIFICATE TYPES</div>
    <ul class="features">
      <li>Unlimited E-Certificates</li><li>Unlimited SMS Certificates</li><li>Unlimited Web Banner Certificates</li><li>Unlimited White Label Certiifcate Landing Pages</li><li>Unlimited Website Sticky Bar Certificates</li><li>Unlimited Website Pop Up Certificate</li><li>Unlimited API E-Certificates</li><li>Unlimited Flowlink Integration Access</li><li>FREE Warm Lead Letter Templates</li><li>FREE Customer Appreciation Letter Templates</li><li>FREE Professional-Grade Incentive Videos</li><li>FREE Proven Social Feed Ad Templates</li><li>FREE High-Converting Banner Ad Templates</li><li>FREE Time-Tested Print Ad Templates</li><li>FREE White Label Redemption Website</li><li>FREE Industry Specific Ad Packs</li><li>FREE Affiliate Program-Earn 50% Commissions</li><li>FREE Eye-Catching Posters, Flyers &amp; Brochures Each Certificate</li><li>FREE Step by Step Redemption Guides</li>
    </ul>
  </div>
  <a class="btn-select bottom-select" href="#">SELECT <svg width="20" height="18" viewBox="0 0 20 18"><path d="M1 9h16M10 2l7 7-7 7" stroke="#fff" stroke-width="3" fill="none"/></svg></a>
</section>

<footer class="site-footer">
  <div class="footer-brand"><span class="dot"></span>BRIGHTLANE PROMO WORKS</div>
  <div class="socials"><span></span><span></span><span></span><span></span></div>
  <div class="free-samples">GET FREE SAMPLES<small>100% FREE</small></div>

  <div class="fdivider" style="left:314px"></div>
  <div class="fcol" style="left:339px;width:340px">
    <h4>Contact Us</h4>
    <div class="contact-row"><svg width="16" height="18" viewBox="0 0 16 18"><path d="M8 17s6-6 6-10A6 6 0 0 0 2 7c0 4 6 10 6 10z" fill="none" stroke="#c9d2dc" stroke-width="1.4"/><circle cx="8" cy="7" r="2" fill="#c9d2dc"/></svg><strong>Brightlane Promo Works Group, Inc.</strong><br>4170 Harbor Crest Way Suite 118<br>Oceanview, CA 90000</div>
    <div class="contact-row"><svg width="16" height="16" viewBox="0 0 16 16"><path d="M3 1l3 3-2 2c1 3 3 5 6 6l2-2 3 3-2 2C7 15 1 9 1 3z" fill="none" stroke="#c9d2dc" stroke-width="1.4"/></svg>USA Office: <strong>1-555-214-3780</strong><br>International: <strong>1-800-555-0142</strong><br>Text Us: <strong>1-555-302-7719</strong></div>
    <div class="contact-row"><svg width="16" height="12" viewBox="0 0 16 12"><rect x="1" y="1" width="14" height="10" fill="none" stroke="#c9d2dc" stroke-width="1.4"/><path d="M1 1l7 6 7-6" fill="none" stroke="#c9d2dc" stroke-width="1.4"/></svg>info@brightlanepromoworks.biz</div>
    <div class="contact-row"><svg width="16" height="16" viewBox="0 0 16 16"><circle cx="8" cy="8" r="7" fill="none" stroke="#c9d2dc" stroke-width="1.4"/><path d="M8 4v4l3 2" fill="none" stroke="#c9d2dc" stroke-width="1.4"/></svg>24/7 Chat Support<br>24/7 Live Answering Service<br>24/7 Email Support<br><span class="green-note">Live Phone &amp; SMS Support:</span><br>Monday - Friday 8am - 5pm PST<br><span class="green-note">Sat/Sun/Holidays Closed</span></div>
  </div>

  <div class="fdivider" style="left:690px"></div>
  <div class="fcol links" style="left:714px;width:190px">
    <h4>Quick Links</h4>
    <a href="#">Home</a><a href="https://www.brightlanepromoworks.biz/incentives">The Incentives</a><a href="#">Samples</a><a href="#">Affiliate</a><a href="#">Testimonials</a><a href="#">Faq</a><a href="#">Contact Us</a><a href="#">Redemption Demo Videos</a><a href="#">BPW Distribute Certificate<br>Demo Videos</a>
  </div>

  <div class="fdivider" style="left:915px"></div>
  <div class="fcol links" style="left:939px;width:240px">
    <h4>Other Links</h4>
    <a href="#">Hoteliers</a><a href="#">BPW Certificates List</a><a href="#">How To Use BPW Certificates</a><a href="#">Social Feed Incentive Campaign</a><a href="#">Pop Ups &amp; Sticky Bars</a><a href="#">Whitepaper - Increase Sales</a><a href="#">Whitepaper - Improve Sales During Strange Times</a><a href="#">Whitepaper - Boost Website Conversions</a>
  </div>

  <div class="copyright">© 2020 <strong>Brightlane Promo Works Group, Inc.</strong> All Rights Reserved. CST# 4418203 <span class="tc">TCRC#</span> 772046</div>
  <div class="legal">Privacy Policy &nbsp;|&nbsp; Term And Conditions</div>
  <div class="chat"><svg width="26" height="24" viewBox="0 0 26 24"><rect x="2" y="2" width="22" height="17" rx="4" fill="#fff"/><path d="M8 19l-2 4 6-4z" fill="#fff"/><path d="M8 12c3 2 7 2 10 0" stroke="#e5231f" stroke-width="2" fill="none"/></svg></div>
</footer>

</body>
</html>
```